Designing business cards for my start-up business

The company is called Velloran. We are a start-up tech data company based in Guernsey, Channel Islands. We want the business cards to look clean, fresh and innovative, just what a tech company should be. We do not want the business cards to look corporate or too official such as a bank. I would like the front of the business card to have our logo and the tag line of "connecting talent". On the back will be our contact details, emails etc. However I am open to your ideas and suggestions. I have provided all our logos and a word doc of all our contact details. There are 4 directors of the business, so I want 4 versions of the same design.

Target Market(s)

Our clients are businesses of all industries. Its a broad target market.

Industry/Entity Type

Information Technology

Contact Information for Business Card

I have attached a word doc called "Business Cards info" which gives all contact details of the 4 employees for the company.

Requirements
Must have
• We must have our logo and the tag line of "connecting talent". This could on the front of the card and then the individuals contact details on the back. Other than that, I'm happy for the designers to come up with ideas/styles.
Nice to have
• N/A
Should not have
• I don't want the cards to look too formal or corporate. As mentioned, we are a tech start-up so we want to look innovative.

```html
<!DOCTYPE html>
<html lang="en">
<head>
<meta charset="utf-8">
<title>Velloran business cards</title>
<link href="https://fonts.googleapis.com/css2?family=Arimo:wght@400;700&family=Montserrat:wght@600&display=swap" rel="stylesheet">
<style>
  :root {
    --bg: #e9e7e3;
    --ink: #0b0b0b;
    --orange: #e8512f;
    --orange-deep: #c9321e;
    --white: #ffffff;
    --divider: #cfcfcf;
  }
  * { box-sizing: border-box; margin: 0; padding: 0; }
  html, body { width: 1200px; height: 864px; overflow: hidden; }
  body {
    background: var(--bg);
    font-family: "Arimo", Arial, sans-serif;
    position: relative;
  }
  .card {
    position: absolute;
    top: 278px;
    width: 540px;
    height: 308px;
    border-radius: 3px;
    overflow: hidden;
    box-shadow: 0 6px 18px rgba(0,0,0,0.18);
  }
  .card--front { left: 40px; background: var(--ink); }
  .card--back {
    left: 620px;
    background: linear-gradient(135deg, var(--orange-deep) 0%, var(--orange) 70%);
  }

  /* front */
  .brand-mark {
    position: absolute; left: 72px; top: 34px;
    width: 100px; height: 100px;
    background: linear-gradient(135deg, var(--orange-deep), var(--orange));
  }
  .brand-name {
    position: absolute; left: 38px; top: 150px;
    font-family: "Montserrat", Arial, sans-serif;
    font-weight: 600; font-size: 22px;
    letter-spacing: 11px;
    color: var(--white);
  }
  .divider {
    position: absolute; left: 262px; top: 36px;
    width: 2px; height: 168px;
    background: var(--divider);
  }
  .person { position: absolute; left: 290px; top: 38px; }
  .person__name { color: var(--orange); font-size: 30px; font-weight: 400; line-height: 1; }
  .person__role { color: var(--white); font-size: 15px; font-weight: 700; margin-top: 4px; letter-spacing: 0.5px; }
  .contacts { position: absolute; left: 290px; top: 134px; list-style: none; }
  .contacts li {
    display: flex; align-items: center; gap: 10px;
    color: var(--white); font-size: 16px; letter-spacing: 0.4px;
    height: 22px;
  }
  .contacts svg { width: 13px; height: 13px; flex: none; }
  .band { position: absolute; left: 0; top: 0; width: 540px; height: 308px; }
  .address {
    font-family: "Arimo", Arial, sans-serif;
    font-size: 13.5px; fill: var(--white); letter-spacing: 0.3px;
  }

  /* back */
  .back-word {
    position: absolute; right: 24px; top: 50%;
    writing-mode: vertical-rl;
    transform: translateY(-50%) rotate(180deg);
    font-family: "Montserrat", Arial, sans-serif;
    font-weight: 600; font-size: 30px;
    letter-spacing: 12px;
    line-height: 1;
    color: var(--white);
    white-space: nowrap;
  }
  .back-square {
    position: absolute; left: 170px; top: 80px;
    width: 120px; height: 120px;
    background: var(--white);
  }
  .tagline {
    position: absolute; left: 170px; top: 218px;
    width: 120px;
    font-family: "Arimo", Arial, sans-serif;
    font-size: 13px; font-weight: 400;
    letter-spacing: 1px;
    text-align: center;
    color: var(--white);
    white-space: nowrap;
  }
</style>
</head>
<body>

  <section class="card card--front" aria-label="Business card front">
    <svg class="band" viewBox="0 0 540 308" aria-hidden="true">
      <defs>
        <path id="address-curve" d="M 30 250 Q 260 262 480 298"/>
      </defs>
      <path d="M 0 222 Q 250 232 540 296 L 540 308 L 0 308 Z" fill="var(--orange)"/>
      <path d="M 150 218 Q 360 226 540 282 L 540 290 Q 360 234 150 218 Z" fill="var(--white)"/>
      <text class="address"><textPath href="#address-curve">12 Rue Marchant, St Peter Port, Guernsey, GY1 4QR, Channel Islands</textPath></text>
    </svg>

    <div class="brand-mark"></div>
    <div class="brand-name">Velloran</div>
    <div class="divider"></div>

    <div class="person">
      <h1 class="person__name">Adam Kerrow</h1>
      <p class="person__role">Director</p>
    </div>

    <ul class="contacts">
      <li>
        <svg viewBox="0 0 13 13" aria-hidden="true"><rect width="13" height="13" fill="var(--orange)"/><circle cx="6.5" cy="6.5" r="3.8" fill="none" stroke="var(--ink)" stroke-width="1.2"/><path d="M2.7 6.5h7.6M6.5 2.7v7.6" stroke="var(--ink)" stroke-width="1"/></svg>
        www.velloran.gg
      </li>
      <li>
        <svg viewBox="0 0 13 13" aria-hidden="true"><rect width="13" height="13" fill="var(--orange)"/><path d="M4 3 L6 3 L6.5 5 L5.5 6 Q6.5 7.8 7.5 8 L8.5 7 L10 7.5 L10 9.5 Q6 10 3.5 5 Z" fill="var(--ink)"/></svg>
        +44 7700 900 214
      </li>
      <li>
        <svg viewBox="0 0 13 13" aria-hidden="true"><rect width="13" height="13" fill="var(--orange)"/><rect x="2.5" y="4" width="8" height="5.5" fill="none" stroke="var(--ink)" stroke-width="1.1"/><path d="M2.5 4 L6.5 7 L10.5 4" fill="none" stroke="var(--ink)" stroke-width="1.1"/></svg>
        Adam.Kerrow@velloran.gg
      </li>
    </ul>
  </section>

  <section class="card card--back" aria-label="Business card back">
    <div class="back-square"></div>
    <p class="tagline">connecting talent</p>
    <div class="back-word">Velloran</div>
  </section>

</body>
</html>
```